Vex

I have the logo for the back already. Need the front to match.
Need a VEX logo which I can provide or you can download one - VEX Realty in canada... Back of the card will be my logo and name. Front will have the info...
I would like a black background. Match colors on front to the back..
Details on Card

Target Market(s)

Realestate clients.. Keep it classy like the logo

Contact Information for Business Card

Moren Tadwick office - 5817730264 cell - 5819063147 email - Moren@MorenTadwick.Com. website - MorenTadwick.Com Facebook - MTadwRealty Instagram - Moren_Qpl_Realtor Address - 418 - 23 St NE | K5P2M8

Colors
3176b5
33a6d7
85cae6

Requirements
Must have
• same color scheme as the logo
logo will be on the back
Black Background
Horizontal card
The one side of the card should be clean. like I stated, just my logo " Moren Tadwick " and nothing else

```html
<!DOCTYPE html>
<html lang="en">
<head>
<meta charset="utf-8">
<title>Moren Tadwick – Business Card</title>
<link href="https://fonts.googleapis.com/css2?family=Cinzel:wght@500&family=Montserrat:wght@400;500&display=swap" rel="stylesheet">
<style>
  :root {
    --page-bg: #dde9ec;
    --card-bg: #1a1f22;
    --brand-blue: #0b80c8;
    --text-light: #e9eef0;
    --white: #ffffff;
  }
  html, body {
    margin: 0;
    padding: 0;
    width: 717px;
    height: 1200px;
    overflow: hidden;
    background: var(--page-bg);
  }
  .canvas {
    position: relative;
    width: 717px;
    height: 1200px;
  }
  .card {
    position: absolute;
    left: 127px;
    width: 462px;
    height: 260px;
    background: var(--card-bg);
    border-radius: 13px;
    box-shadow: 0 0 0 1px rgba(0,0,0,0.15);
  }
  .card--back { top: 305px; }
  .card--front { top: 635px; }

  .back-name {
    position: absolute;
    left: 0;
    right: 0;
    top: 106px;
    margin: 0;
    text-align: center;
    font-family: "Cinzel", serif;
    font-weight: 500;
    font-size: 31px;
    letter-spacing: 0.5px;
    color: var(--brand-blue);
  }

  .contact-list {
    position: absolute;
    left: 42px;
    top: 38px;
    margin: 0;
    padding: 0;
    list-style: none;
  }
  .contact-item {
    display: flex;
    align-items: center;
    height: 18px;
    margin-bottom: 7.3px;
    font-family: "Montserrat", sans-serif;
    font-size: 10.5px;
    color: var(--text-light);
  }
  .contact-icon {
    width: 18px;
    height: 18px;
    margin-right: 14px;
    flex: none;
  }

  .brokerage-mark {
    position: absolute;
    left: 330px;
    top: 38px;
    width: 93px;
    height: 80px;
    background: var(--brand-blue);
    display: flex;
    align-items: center;
    justify-content: center;
    text-align: center;
    font-family: "Cinzel", serif;
    font-weight: 500;
    font-size: 15px;
    line-height: 1.2;
    color: var(--white);
  }
</style>
</head>
<body>
<main class="canvas">

  <section class="card card--back" aria-label="Card back">
    <h1 class="back-name">MOREN TADWICK</h1>
  </section>

  <section class="card card--front" aria-label="Card front">
    <ul class="contact-list">
      <li class="contact-item">
        <svg class="contact-icon" viewBox="0 0 18 18" aria-hidden="true"><rect width="18" height="18" rx="2" fill="var(--brand-blue)"/><path d="M5.5 4.5l2 0 1 3-1.3 1a6 6 0 0 0 2.8 2.8l1-1.3 3 1v2c0 .6-.5 1-1 1A8.5 8.5 0 0 1 4.5 5.5c0-.5.4-1 1-1z" fill="#fff"/></svg>
        581-773-0264
      </li>
      <li class="contact-item">
        <svg class="contact-icon" viewBox="0 0 18 18" aria-hidden="true"><rect width="18" height="18" rx="2" fill="var(--brand-blue)"/><rect x="5.5" y="3.5" width="7" height="11" rx="1.2" fill="none" stroke="#fff" stroke-width="1.4"/><circle cx="9" cy="12.5" r=".8" fill="#fff"/></svg>
        581-906-3147
      </li>
      <li class="contact-item">
        <svg class="contact-icon" viewBox="0 0 18 18" aria-hidden="true"><rect width="18" height="18" rx="2" fill="var(--brand-blue)"/><path d="M9 3.5l6 5.2h-1.7V14H10.5v-3.2h-3V14H4.7V8.7H3z" fill="#fff"/></svg>
        418 - 23 St NE | K5P2M8
      </li>
      <li class="contact-item">
        <svg class="contact-icon" viewBox="0 0 18 18" aria-hidden="true"><rect width="18" height="18" rx="2" fill="var(--brand-blue)"/><rect x="3.5" y="5" width="11" height="8" fill="none" stroke="#fff" stroke-width="1.3"/><path d="M3.5 5L9 9.5 14.5 5M3.5 13L7.5 9M14.5 13L10.5 9" fill="none" stroke="#fff" stroke-width="1.1"/></svg>
        Moren@MorenTadwick.Com
      </li>
      <li class="contact-item">
        <svg class="contact-icon" viewBox="0 0 18 18" aria-hidden="true"><rect width="18" height="18" rx="2" fill="var(--brand-blue)"/><circle cx="9" cy="9" r="5.2" fill="none" stroke="#fff" stroke-width="1.2"/><ellipse cx="9" cy="9" rx="2.2" ry="5.2" fill="none" stroke="#fff" stroke-width="1"/><path d="M3.8 9h10.4" stroke="#fff" stroke-width="1"/></svg>
        MorenTadwick.Com
      </li>
      <li class="contact-item">
        <svg class="contact-icon" viewBox="0 0 18 18" aria-hidden="true"><rect width="18" height="18" rx="2" fill="var(--brand-blue)"/></svg>
        MTadwRealty
      </li>
      <li class="contact-item">
        <svg class="contact-icon" viewBox="0 0 18 18" aria-hidden="true"><rect width="18" height="18" rx="2" fill="var(--brand-blue)"/></svg>
        Moren_Qpl_Realtor
      </li>
    </ul>

    <div class="brokerage-mark">VEX<br>REALTY</div>
  </section>

</main>
</body>
</html>
```